Business Card design for a skin clinic

i would like a business card design for our skin clinic.
our logo colors are Blue and Grey and Bule /white.
we are searching for a minimalistic design yet very elegant,dynamic and professional which can reflect a professional medical skin care clinic( not a beauty salon).
THE DESGIN IS NOT FOR A PERSON IT WILL BE USED IN THE CLINIC FOR CLIENTS SO THERE SHOULD BE NO NAME OF A PERSON ONLY THE CLINIC NAME AND THE CONTACT INFO

Target Market(s)
young and old womens
Industry/Entity Type
Business
Contact Information for Business Card
we have 2 address and both should be on the card.
address A: Lindenhoflaan 214B, 3041KP Rotterdam, Tel 010 483 21 95
address B: Zonnewijzerstraat 238, 1062RT Amsterdam Tel 020 571 3829
website www.huidpuntzorg.nu, email info@huidpuntzorg.nu
Look and feel
Each slider illustrates characteristics of the customer's brand and the style your logo design should communicate.

```html
<!DOCTYPE html>
<html lang="nl">
<head>
<meta charset="utf-8">
<title>Huidpuntzorg – business card concepts</title>
<link rel="stylesheet" href="https://fonts.googleapis.com/css2?family=Montserrat:wght@500&family=Open+Sans:wght@400&family=Tinos:wght@400&display=swap">
<style>
  :root{
    --page:#ffffff;
    --ink:#111111;
    --brand-blue:#3a8fd0;
    --brand-grey:#6d6e71;
    --card1-bg:#eceeee;
    --card1-strip:#2a9ad6;
    --card1-front:#dcf0fa;
    --card1-panel:#b6e0f5;
    --card2-band:#6a9bd6;
    --card2-front:#0f5a94;
    --card3-blue-a:#2f87cc;
    --card3-blue-b:#3aa2da;
    --card3-pill:#1c6fb4;
    --card3-front:#78bcd9;
    --card3-pattern:#86c4de;
    --faint:#d5dde6;
  }
  html,body{margin:0;padding:0;overflow:hidden;background:var(--page);}
  .sheet{position:relative;width:1200px;height:848px;overflow:hidden;background:var(--page);}
  .brand{font-family:"Montserrat",sans-serif;font-weight:500;letter-spacing:.5px;margin:0;white-space:nowrap;}
  .tagline{font-family:"Montserrat",sans-serif;font-weight:500;margin:0;white-space:nowrap;letter-spacing:.4px;}
  .detail{font-family:"Tinos",serif;}
  .sheet-brand{position:absolute;left:985px;top:72px;width:150px;text-align:center;}
  .sheet-brand .brand{font-size:16px;color:var(--brand-blue);}
  .sheet-brand .tagline{font-size:7.5px;color:var(--brand-grey);margin-top:3px;}
  .option-number{position:absolute;font-family:"Open Sans",sans-serif;font-size:32px;color:var(--ink);margin:0;}
  .side-label{position:absolute;font-family:"Open Sans",sans-serif;font-size:32px;color:var(--ink);margin:0;transform:translateX(-50%);}
  .card{position:absolute;overflow:hidden;}
  .card svg{display:block;}

  /* option 1 */
  .c1-back{left:332px;top:112px;width:240px;height:156px;background:var(--card1-bg);}
  .c1-back .brand{position:absolute;left:11px;top:17px;font-size:12.5px;color:var(--brand-blue);}
  .c1-back .tagline{position:absolute;left:11px;top:33px;font-size:5px;color:var(--brand-grey);}
  .c1-back .rule{position:absolute;left:10px;top:40px;width:105px;height:1.5px;background:#7fa6c9;}
  .c1-back .deco{position:absolute;left:118px;top:48px;width:110px;height:110px;border-radius:50%;background:var(--faint);opacity:.7;}
  .c1-back .strip{position:absolute;left:0;bottom:0;width:100%;height:6px;background:var(--card1-strip);}
  .c1-back .info{position:absolute;font-size:5.6px;line-height:1.3;color:#222;}
  .c1-back .divider{position:absolute;top:82px;height:52px;border-left:1.5px dotted var(--brand-blue);}
  .c1-front{left:625px;top:115px;width:240px;height:155px;background:var(--card1-front);}
  .c1-front .frame-back{position:absolute;left:22px;top:51px;width:188px;height:61px;border:1px solid var(--brand-blue);}
  .c1-front .frame-front{position:absolute;left:30px;top:43px;width:187px;height:63px;border:1px solid var(--brand-blue);background:var(--card1-panel);text-align:center;}
  .c1-front .brand{font-size:13px;color:var(--brand-blue);margin-top:33px;}
  .c1-front .tagline{font-size:5.5px;color:var(--brand-grey);margin-top:3px;}

  /* option 2 */
  .c2-back{left:332px;top:348px;width:240px;height:154px;background:#fff;}
  .c2-back .brand{position:absolute;left:55px;top:9px;font-size:12px;color:var(--brand-blue);}
  .c2-back .tagline{position:absolute;left:66px;top:25px;font-size:5px;color:var(--brand-grey);}
  .c2-front{left:629px;top:347px;width:242px;height:155px;background:var(--card2-front);text-align:center;}
  .c2-front .brand{font-size:20px;color:#cfe4f6;margin-top:86px;letter-spacing:1px;}
  .c2-front .tagline{font-size:8.5px;color:#cfe4f6;margin-top:4px;}

  /* option 3 */
  .c3-back{left:333px;top:582px;width:241px;height:156px;background:#f8f9fa;}
  .c3-back .panel{position:absolute;left:119px;top:0;width:122px;height:156px;background:linear-gradient(90deg,var(--card3-blue-a),var(--card3-blue-b));}
  .c3-back .pill{position:absolute;left:24px;top:46px;width:170px;height:38px;border-radius:19px;background:var(--card3-pill);text-align:center;}
  .c3-back .pill .brand{font-size:15px;color:#dbe9f6;margin-top:6px;}
  .c3-back .pill .tagline{font-size:6px;color:#dbe9f6;margin-top:3px;}
  .c3-back .deco{position:absolute;left:0;top:110px;width:44px;height:44px;border-radius:50%;background:var(--faint);opacity:.6;}
  .c3-back .info{position:absolute;left:150px;font-size:5.8px;line-height:1.35;color:#fff;}
  .c3-back .info .line{display:block;border-bottom:1px solid rgba(255,255,255,.7);padding-bottom:1px;margin-bottom:2px;}
  .c3-back .icon{position:absolute;left:133px;}
  .c3-front{left:631px;top:579px;width:241px;height:156px;background:var(--card3-front);text-align:center;}
  .c3-front .pattern{position:absolute;top:32px;width:46px;height:60px;background:var(--card3-pattern);z-index:0;}
  .c3-front .wordmark{position:relative;z-index:1;padding-top:82px;}
  .c3-front .brand{font-size:17px;color:var(--brand-grey);letter-spacing:1px;}
  .c3-front .tagline{font-size:6.5px;color:var(--brand-grey);margin-top:3px;}
</style>
</head>
<body>
<main class="sheet">
  <header class="sheet-brand">
    <p class="brand">HUIDPUNTZORG</p>
    <p class="tagline">next generation skin care</p>
  </header>

  <p class="option-number" style="left:283px;top:118px;">1</p>
  <p class="option-number" style="left:283px;top:376px;">2</p>
  <p class="option-number" style="left:286px;top:622px;">3</p>

  <!-- Option 1 -->
  <section class="card c1-back" aria-label="Option 1 back">
    <div class="deco"></div>
    <p class="brand">HUIDPUNTZORG</p>
    <div class="rule"></div>
    <p class="tagline">next generation skin care</p>
    <svg style="position:absolute;left:7px;top:92px" width="12" height="12" viewBox="0 0 12 12"><circle cx="6" cy="6" r="5.5" fill="var(--brand-blue)"/><path d="M6 3a2 2 0 0 1 2 2c0 1.5-2 3.5-2 3.5S4 6.5 4 5a2 2 0 0 1 2-2z" fill="#fff"/></svg>
    <p class="info detail" style="left:24px;top:83px;margin:0;">- Lindenhoflaan 214B,<br>3041KP Rotterdam<br>&amp;<br>- Zonnewijzerstraat 238,<br>1062RT Amsterdam</p>
    <div class="divider" style="left:89px;"></div>
    <svg style="position:absolute;left:96px;top:92px" width="12" height="12" viewBox="0 0 12 12"><circle cx="6" cy="6" r="5.5" fill="var(--brand-blue)"/><rect x="4" y="3" width="4" height="6" rx="1" fill="#fff"/></svg>
    <p class="info detail" style="left:114px;top:88px;margin:0;text-align:center;">010 483 21 95<br>&amp;<br>020 571 3829</p>
    <div class="divider" style="left:156px;"></div>
    <svg style="position:absolute;left:162px;top:82px" width="14" height="14" viewBox="0 0 14 14" fill="none" stroke="var(--brand-blue)" stroke-width="1"><circle cx="7" cy="7" r="6"/><ellipse cx="7" cy="7" rx="2.5" ry="6"/><path d="M1 7h12"/></svg>
    <svg style="position:absolute;left:162px;top:102px" width="14" height="14" viewBox="0 0 14 14" fill="none" stroke="var(--brand-blue)" stroke-width="1"><circle cx="7" cy="7" r="6"/><text x="7" y="9.5" font-size="7" text-anchor="middle" fill="var(--brand-blue)" stroke="none" font-family="Arial, sans-serif">@</text></svg>
    <p class="info detail" style="left:180px;top:86px;margin:0;text-align:center;">www.huidpuntzorg.nu<br>&amp;<br>info@huidpuntzorg.nu</p>
    <div class="strip"></div>
  </section>
  <p class="side-label" style="left:438px;top:273px;">back</p>

  <section class="card c1-front" aria-label="Option 1 front">
    <div class="frame-back"></div>
    <div class="frame-front">
      <p class="brand">HUIDPUNTZORG</p>
      <p class="tagline">next generation skin care</p>
    </div>
  </section>
  <p class="side-label" style="left:731px;top:276px;">front</p>

  <!-- Option 2 -->
  <section class="card c2-back" aria-label="Option 2 back">
    <p class="brand">HUIDPUNTZORG</p>
    <p class="tagline">next generation skin care</p>
    <svg width="240" height="154" viewBox="0 0 240 154" style="position:absolute;left:0;top:0">
      <polygon points="0,79 240,41 240,120 40,154 0,154" fill="var(--card2-band)"/>
      <line x1="0" y1="107" x2="240" y2="69" stroke="#fff" stroke-width="2"/>
      <line x1="0" y1="132" x2="240" y2="94" stroke="#fff" stroke-width="2"/>
      <g transform="skewY(-9)" font-family="Arial, sans-serif" font-size="5.8" fill="#fff">
        <circle cx="12" cy="93" r="6" fill="none" stroke="#fff" stroke-width="1"/>
        <path d="M12 89.5a2 2 0 0 1 2 2c0 1.5-2 3.5-2 3.5s-2-2-2-3.5a2 2 0 0 1 2-2z" fill="#fff"/>
        <text x="22" y="91">Lindenhoflaan 214B,</text>
        <text x="22" y="98">3041KP Rotterdam</text>
        <line x1="92" y1="85" x2="92" y2="100" stroke="#fff" stroke-width=".8"/>
        <text x="97" y="91">Zonnewijzerstraat 238,</text>
        <text x="97" y="98">1062RT Amsterdam</text>
        <circle cx="12" cy="119" r="6" fill="none" stroke="#fff" stroke-width="1"/>
        <rect x="10" y="116" width="4" height="6" rx="1" fill="#fff"/>
        <text x="24" y="121">010 483 21 95</text>
        <line x1="66" y1="114" x2="66" y2="124" stroke="#fff" stroke-width=".8"/>
        <text x="72" y="121">020 571 3829</text>
        <circle cx="158" cy="119" r="6" fill="none" stroke="#fff" stroke-width="1"/>
        <path d="M152 119h12M158 113v12" stroke="#fff" stroke-width=".7"/>
        <text x="169" y="121">www.huidpuntzorg.nu</text>
        <circle cx="95" cy="145" r="6" fill="none" stroke="#fff" stroke-width="1"/>
        <text x="95" y="147.5" text-anchor="middle" font-size="7">@</text>
        <text x="106" y="147">info@huidpuntzorg.nu</text>
      </g>
    </svg>
  </section>
  <p class="side-label" style="left:438px;top:504px;">back</p>

  <section class="card c2-front" aria-label="Option 2 front">
    <p class="brand">HUIDPUNTZORG</p>
    <p class="tagline">next generation skin care</p>
  </section>
  <p class="side-label" style="left:738px;top:511px;">front</p>

  <!-- Option 3 -->
  <section class="card c3-back" aria-label="Option 3 back">
    <div class="panel"></div>
    <div class="deco"></div>
    <div class="pill">
      <p class="brand">HUIDPUNTZORG</p>
      <p class="tagline">next generation skin care</p>
    </div>
    <svg class="icon" style="top:8px" width="12" height="12" viewBox="0 0 12 12" fill="none" stroke="#fff" stroke-width=".9"><circle cx="6" cy="6" r="5"/><ellipse cx="6" cy="6" rx="2" ry="5"/><path d="M1 6h10"/></svg>
    <p class="info detail" style="top:9px;margin:0;"><span class="line">www.huidpuntzorg.nu</span></p>
    <svg class="icon" style="top:26px" width="12" height="12" viewBox="0 0 12 12"><circle cx="6" cy="6" r="5" fill="none" stroke="#fff" stroke-width=".9"/><text x="6" y="8.3" font-size="6.5" text-anchor="middle" fill="#fff" font-family="Arial, sans-serif">@</text></svg>
    <p class="info detail" style="top:27px;margin:0;"><span class="line">info@huidpuntzorg.nu</span></p>
    <svg class="icon" style="top:96px" width="12" height="12" viewBox="0 0 12 12"><circle cx="6" cy="6" r="5" fill="none" stroke="#fff" stroke-width=".9"/><path d="M6 3a2 2 0 0 1 2 2c0 1.5-2 3.5-2 3.5S4 6.5 4 5a2 2 0 0 1 2-2z" fill="#fff"/></svg>
    <p class="info detail" style="top:92px;margin:0;"><span class="line">Lindenhoflaan 214B,<br>3041KP Rotterdam</span>Zonnewijzerstraat 238,<br>1062RT Amsterdam</p>
    <svg class="icon" style="top:131px" width="12" height="12" viewBox="0 0 12 12"><circle cx="6" cy="6" r="5" fill="none" stroke="#fff" stroke-width=".9"/><rect x="4" y="3" width="4" height="6" rx="1" fill="#fff"/></svg>
    <p class="info detail" style="top:130px;margin:0;"><span class="line">010 483 21 95</span>020 571 3829</p>
  </section>
  <p class="side-label" style="left:430px;top:752px;">back</p>

  <section class="card c3-front" aria-label="Option 3 front">
    <div class="pattern" role="img" aria-label="Decorative linked pattern" style="left:2px;"></div>
    <div class="pattern" role="img" aria-label="Decorative linked pattern" style="right:2px;"></div>
    <div class="wordmark">
      <p class="brand">HUIDPUNTZORG</p>
      <p class="tagline">next generation skin care</p>
    </div>
  </section>
  <p class="side-label" style="left:739px;top:753px;">front</p>
</main>
</body>
</html>
```